KTR Football Academy Term 1 Certificate

Hello,
I require a certificate design which will be an improvement on previous designs attached.
The certificate must incorporate both logos and have the wording below.

Kestrel Track Rovers Football Academy
Certificate Of Participation
Presented to
______________________________________________________

For completing KTR Football Academy Term 1, 2024

```html
<!DOCTYPE html>
<html lang="en">
<head>
<meta charset="utf-8">
<title>KTR Football Academy – Certificate of Participation</title>
<link rel="stylesheet" href="https://fonts.googleapis.com/css2?family=Archivo:wght@600;700;800&family=Libre+Baskerville:wght@400;700&display=swap">
<style>
  :root {
    --backdrop: #333333;
    --paper: #ffffff;
    --green: #86c155;
    --green-deep: #4f7f36;
    --green-mid: #5e8f3c;
    --green-light: #a5d14b;
    --gold: #d9a846;
    --charcoal: #1f1f21;
    --slate: #6d6e71;
    --rule: #7a7a7c;
  }
  * { margin: 0; padding: 0; box-sizing: border-box; }
  html, body {
    width: 1200px; height: 1200px; overflow: hidden;
    background: var(--backdrop);
  }
  .certificate {
    position: absolute;
    left: 68px; top: 220px;
    width: 1064px; height: 760px;
    background: var(--paper);
    box-shadow: 0 6px 18px rgba(0,0,0,0.35);
    overflow: hidden;
  }
  .certificate-art { position: absolute; inset: 0; width: 100%; height: 100%; }
  .academy-name {
    font-family: "Archivo", Arial, sans-serif; font-weight: 700;
    font-size: 25px; fill: var(--paper);
  }
  .title-main {
    font-family: "Libre Baskerville", Georgia, serif; font-weight: 700;
    font-size: 116px; fill: var(--green);
  }
  .title-sub {
    font-family: "Archivo", Arial, sans-serif; font-weight: 800;
    font-size: 52px; fill: var(--slate);
  }
  .presented {
    font-family: "Libre Baskerville", Georgia, serif; font-weight: 400;
    font-size: 37px; fill: var(--green);
  }
  .completion {
    font-family: "Archivo", Arial, sans-serif; font-weight: 700;
    font-size: 21px; fill: var(--slate);
  }
  .term {
    font-family: "Archivo", Arial, sans-serif; font-weight: 700;
    font-size: 28px; fill: var(--green);
  }
  .brand-name {
    font-family: "Archivo", Arial, sans-serif; font-weight: 700;
    font-size: 20px; fill: var(--green);
  }
  .brand-short {
    font-family: "Archivo", Arial, sans-serif; font-weight: 700;
    font-size: 30px; fill: var(--green);
  }
</style>
</head>
<body>
<main class="certificate">
  <svg class="certificate-art" viewBox="0 0 1064 760" xmlns="http://www.w3.org/2000/svg">
    <defs>
      <linearGradient id="greenBandTop" x1="0" y1="0" x2="1" y2="1">
        <stop offset="0" stop-color="#8cc04a"/>
        <stop offset="0.35" stop-color="#5e8f3c"/>
        <stop offset="0.6" stop-color="#a5d14b"/>
        <stop offset="1" stop-color="#4f7f36"/>
      </linearGradient>
      <linearGradient id="greenBandBottom" x1="1" y1="1" x2="0" y2="0">
        <stop offset="0" stop-color="#8cc04a"/>
        <stop offset="0.3" stop-color="#a5d14b"/>
        <stop offset="0.55" stop-color="#5e8f3c"/>
        <stop offset="1" stop-color="#4f7f36"/>
      </linearGradient>
      <linearGradient id="darkBar" x1="0" y1="1" x2="1" y2="0">
        <stop offset="0" stop-color="#1f1f21"/>
        <stop offset="1" stop-color="#6d6e71"/>
      </linearGradient>
      <linearGradient id="darkBarRight" x1="1" y1="0" x2="0" y2="1">
        <stop offset="0" stop-color="#1f1f21"/>
        <stop offset="1" stop-color="#6d6e71"/>
      </linearGradient>
    </defs>

    <!-- gold inner frame -->
    <rect class="frame" x="30" y="30" width="1005" height="698" rx="10" fill="none" stroke="var(--gold)" stroke-width="1.5"/>

    <!-- top-left corner bands -->
    <line class="corner-bar" x1="243" y1="186" x2="-220" y2="649" stroke="url(#darkBar)" stroke-width="56" stroke-linecap="round"/>
    <polygon class="corner-green" points="0,0 390,0 0,390" fill="url(#greenBandTop)"/>
    <line class="corner-gold" x1="361" y1="0" x2="0" y2="361" stroke="var(--gold)" stroke-width="1.5"/>

    <!-- bottom-right corner bands -->
    <line class="corner-bar" x1="904" y1="630" x2="1320" y2="214" stroke="url(#darkBarRight)" stroke-width="56" stroke-linecap="round"/>
    <polygon class="corner-green" points="797,760 1064,760 1064,493" fill="url(#greenBandBottom)"/>
    <line class="corner-gold" x1="818" y1="760" x2="1064" y2="512" stroke="var(--gold)" stroke-width="1.5"/>

    <!-- academy name -->
    <text class="academy-name" x="35" y="59">Kestrel Track</text>
    <text class="academy-name" x="35" y="97">Rovers Football</text>
    <text class="academy-name" x="35" y="136">Academy</text>

    <!-- brand marks -->
    <g class="brand brand-parent">
      <circle cx="742" cy="112" r="26" fill="var(--green)"/>
      <text class="brand-name" x="778" y="94">KESTREL</text>
      <text class="brand-name" x="778" y="117">TRACK</text>
      <text class="brand-name" x="778" y="140">ROVERS</text>
    </g>
    <g class="brand brand-academy">
      <rect x="925" y="93" width="36" height="36" fill="var(--slate)"/>
      <text class="brand-short" x="968" y="123">KTR</text>
    </g>

    <!-- headings -->
    <text class="title-main" x="528" y="325" text-anchor="middle" textLength="560" lengthAdjust="spacingAndGlyphs">Certificate</text>
    <text class="title-sub" x="528" y="385" text-anchor="middle" textLength="554" lengthAdjust="spacing">Of Participation</text>
    <text class="presented" x="528" y="497" text-anchor="middle">Presented to</text>

    <!-- name line -->
    <line class="name-rule" x1="242" y1="577" x2="818" y2="577" stroke="var(--rule)" stroke-width="1.2"/>

    <!-- completion box -->
    <polygon class="completion-box" points="321,636 739,636 747,644 747,668 739,676 321,676 313,668 313,644" fill="none" stroke="var(--green)" stroke-width="1.3"/>
    <text class="completion" x="530" y="664" text-anchor="middle">For completing KTR Football Academy</text>

    <!-- term -->
    <polygon class="dash" points="378,702 428,699 428,705" fill="var(--charcoal)"/>
    <polygon class="dash" points="635,699 685,702 635,705" fill="var(--charcoal)"/>
    <text class="term" x="530" y="712" text-anchor="middle">Term 1, 2024</text>
  </svg>
</main>
</body>
</html>
```